Venlox - Property Management Company Listings - PSD / uncoded only

Our site simply connects property owners with property managers. I’m asking you to create 2 pages, 1 homepage and 1 page that lists of property management companies. Build with Responsive Design in mind. PSD/uncoded files only. Help us create a great site!
Example competitor sites:
http://www.everyestatehelp.example/
http://www.tendyourlots.example/
Inspired by these sites:
http://www.quorvik.example/
http://www.bespokely.example/
http://www.coinwire.example/
https://www.tripboard.example/
I've attached the logo as well as 2 picture files that you can consider using.
• Venlox Logo Colors: Yellow: HTML code: #FBC30A, RGB code: R: 251 G: 195 B: 10 Grey: HTML code: #4E4C4D, RGB code: R: 78 G: 76 B: 77
• The picture files are optional.
o One picture is of houses and neighborhood.
o The other is of a professional woman on the phone. Please do not use the professional woman as a large primary image. You can use the professional woman photo as a smaller photo and not the main photo.
• Please bring your own pictures and graphics too. Don't feel like you need to use mine.
Thank you!

```html
<!DOCTYPE html>
<html lang="en">
<head>
<meta charset="utf-8">
<title>Venlox – Property Management Solutions</title>
<link href="https://fonts.googleapis.com/css2?family=Lato:wght@400;700;900&display=swap" rel="stylesheet">
<style>
  :root {
    --brand-yellow: #FBC30A;
    --brand-grey: #4E4C4D;
    --white: #ffffff;
    --band-dark: #2b2b2b;
    --footer-black: #050505;
    --panel-shade: rgba(40, 40, 45, 0.55);
    --page-bg: #ffffff;
  }
  * { box-sizing: border-box; margin: 0; padding: 0; }
  html, body {
    width: 1200px; height: 1000px; overflow: hidden;
    background: var(--page-bg);
    font-family: "Lato", Arial, sans-serif;
  }
  .site {
    position: absolute; left: 53px; top: 51px;
    width: 1110px; height: 902px; overflow: hidden;
  }
  .hero {
    position: absolute; left: 0; top: 0; width: 1110px; height: 582px;
  }
  .hero-photo {
    position: absolute; inset: 0;
    background:
      linear-gradient(180deg, rgba(94,140,52,0.95) 0%, rgba(112,120,90,0.9) 14%, rgba(104,100,96,0.92) 40%, rgba(96,98,92,0.95) 70%, rgba(88,110,70,0.95) 100%),
      linear-gradient(90deg, #6b6a66, #8a7f70 50%, #6d6f6a);
  }
  .brand {
    position: absolute; left: 220px; top: 10px; width: 140px; text-align: center;
  }
  .brand-name {
    display: inline-flex; align-items: center; gap: 6px;
    font-weight: 700; font-size: 32px; color: var(--white); line-height: 1;
    margin-top: 14px;
  }
  .brand-mark { width: 12px; height: 12px; background: var(--brand-yellow); }
  .brand-tagline { font-size: 7px; color: var(--white); margin-top: 12px; white-space: nowrap; }
  .main-nav {
    position: absolute; top: 36px; left: 577px;
    display: flex; align-items: center; font-size: 10px; color: var(--white);
  }
  .main-nav a { color: var(--white); text-decoration: none; margin-right: 28px; }
  .main-nav a.active { color: var(--brand-yellow); }
  .hero-slogan {
    position: absolute; top: 157px; left: 0; width: 1110px; text-align: center;
    font-weight: 900; font-size: 21px; letter-spacing: 3px; color: var(--white);
  }
  .hero-slogan span { color: var(--brand-yellow); }
  .finder-panel {
    position: absolute; left: 394px; top: 210px; width: 320px; height: 200px;
    background: var(--panel-shade);
  }
  .finder-title {
    position: absolute; left: 405px; top: 211px;
    font-weight: 700; font-size: 33px; line-height: 42px; color: var(--white);
  }
  .field {
    position: absolute; top: 308px; height: 25px;
    border: 1px solid var(--white); color: var(--white);
    font-size: 14px; line-height: 23px; padding: 0 6px;
  }
  .field-type { left: 408px; width: 204px; }
  .field-type svg { position: absolute; right: 6px; top: 6px; }
  .field-zip { left: 625px; width: 77px; }
  .search-button {
    position: absolute; left: 408px; top: 342px; width: 133px; height: 24px;
    background: var(--brand-yellow); color: var(--white);
    font-weight: 700; font-size: 17px; letter-spacing: 1.5px;
    line-height: 24px; padding-left: 20px;
  }
  .search-button .divider { position: absolute; left: 108px; top: 3px; width: 1px; height: 18px; background: var(--white); }
  .search-button svg { position: absolute; left: 114px; top: 5px; }
  .finder-note {
    position: absolute; left: 407px; top: 377px; font-size: 10px; line-height: 12px; color: var(--white);
  }
  .benefits {
    position: absolute; left: 404px; top: 457px; list-style: none;
    font-size: 10px; line-height: 15px; color: var(--white);
  }
  .benefits li::before { content: "•"; margin-right: 6px; }
  .scroll-cue { position: absolute; left: 525px; top: 574px; }
  .manager-band {
    position: absolute; left: 0; top: 582px; width: 1110px; height: 282px;
    background: radial-gradient(ellipse at 50% 40%, #383838 0%, var(--band-dark) 60%, #232323 100%);
    text-align: center; color: var(--white);
  }
  .manager-band h2 { font-weight: 700; font-size: 27px; margin-top: 92px; }
  .manager-band p { font-size: 10px; line-height: 12px; margin-top: 30px; }
  .learn-more {
    display: inline-block; margin-top: 24px; padding: 3px 4px;
    border: 1px solid var(--brand-yellow); color: var(--brand-yellow); font-size: 14px;
  }
  .site-footer {
    position: absolute; left: 0; top: 864px; width: 1110px; height: 38px;
    background: var(--footer-black); color: var(--white); font-size: 7px;
  }
  .copyright { position: absolute; left: 235px; top: 15px; }
  .footer-nav { position: absolute; left: 546px; top: 16px; display: flex; }
  .footer-nav a { color: var(--white); text-decoration: none; padding: 0 7px; border-left: 1px solid var(--white); line-height: 9px; }
  .footer-nav a:first-child { border-left: none; padding-left: 0; color: var(--brand-yellow); }
</style>
</head>
<body>
<div class="site">
  <header class="hero">
    <div class="hero-photo" role="img" aria-label="Aerial photograph of a suburban neighbourhood with houses, trees and green lawns"></div>
    <div class="brand">
      <div class="brand-name"><span class="brand-mark"></span>Venlox</div>
      <div class="brand-tagline">Property Management Solutions, Simplified</div>
    </div>
    <nav class="main-nav">
      <a class="active" href="#">Home</a>
      <a href="#">Are you a Property Manager?</a>
      <a href="#">Contact Us</a>
      <svg width="10" height="10" viewBox="0 0 10 10"><circle cx="4" cy="4" r="3" fill="none" stroke="#fff" stroke-width="1.2"/><line x1="6.2" y1="6.2" x2="9" y2="9" stroke="#fff" stroke-width="1.2"/></svg>
    </nav>
    <h1 class="hero-slogan">PROPERTY MANAGEMENT SOLUTIONS, <span>SIMPLIED.</span></h1>
    <div class="finder-panel"></div>
    <h2 class="finder-title">Find your Local<br>Property Manager</h2>
    <div class="field field-type">Select Your Property Type
      <svg width="18" height="11" viewBox="0 0 18 11"><polyline points="1,1 9,9 17,1" fill="none" stroke="#fff" stroke-width="2"/></svg>
    </div>
    <div class="field field-zip">In zipcode</div>
    <div class="search-button">search<span class="divider"></span>
      <svg width="14" height="14" viewBox="0 0 14 14"><circle cx="6" cy="6" r="4.3" fill="none" stroke="#fff" stroke-width="1.5"/><line x1="9.2" y1="9.2" x2="13" y2="13" stroke="#fff" stroke-width="1.6"/></svg>
    </div>
    <p class="finder-note">Search our directory to find experienced and professional<br>property management companies that meet your needs.</p>
    <ul class="benefits">
      <li>Making renting YOUR home an easy, stress-free experience.</li>
      <li>Connecting property owners with property managers.</li>
      <li>Providing property management solutions, simplified.</li>
    </ul>
    <svg class="scroll-cue" width="60" height="16" viewBox="0 0 60 16"><polygon points="0,0 30,14 60,0 60,2 30,16 0,2" fill="#FBC30A"/><polygon points="6,8 30,16 54,8" fill="#2b2b2b"/></svg>
  </header>
  <section class="manager-band">
    <h2>Are you a Property Manager?</h2>
    <p>Join our real estate property management company network.<br>Let us help you find leads of property owners seeking to rent their homes.</p>
    <a class="learn-more">Learn more</a>
  </section>
  <footer class="site-footer">
    <div class="copyright">Copyright © 2014, Venlox, All Rights Reserved</div>
    <nav class="footer-nav">
      <a href="#">Home</a><a href="#">Are you a Property Manager?</a><a href="#">Contact Us</a><a href="#">Terms of Use</a><a href="#">Privacy Policy</a><a href="#">Site map</a>
    </nav>
  </footer>
</div>
</body>
</html>
```